Keep the Helm Podcast Cover Art

Need cover art for a new podcast called Keep the Helm. The O in Boss should be red. The cover art should be reflective of people, passion, and purpose and have a very high-end, professional speaker/influencer vibe to it. I threw something together borrowing from the LARO VENTI typeface and logo which I've attached. But, it's super basic in feel, and I would like to see something more sophisticated. I've also included two headshots the can possibly be used, but are definitely not a requirement. If one of the images is used, the red hat MUST stay red, but the rest can be B&W and I almost prefer it.
Colors preferred are Black, White, Red and either Gold or Silver. Not sure which I actually like better.
Please do not use the word "podcast" anywhere on the design.

Industry/Entity Type

Business, Entrepreneur, Public Speaker

Requirements
Should not have
• Traditional heart shapes

```html
<!DOCTYPE html>
<html lang="en">
<head>
<meta charset="utf-8">
<title>Keep the Helm – Cover Art Options</title>
<link rel="stylesheet" href="https://fonts.googleapis.com/css2?family=Outfit:wght@400;800&display=swap">
<style>
  :root {
    --stage: #1b1a19;
    --gold: #c9ad4c;
    --ink: #161412;
    --cream: #f2eee6;
    --red-bright: #c40d0d;
    --red-mid: #8e0606;
    --red-deep: #3a0202;
    --hat-red: #a3161c;
    --grey-light: #9a9590;
    --grey-dark: #2a2826;
    --shadow: #000000;
  }
  html, body {
    margin: 0;
    padding: 0;
    width: 1200px;
    height: 3168px;
    overflow: hidden;
    background: var(--stage);
  }
  .canvas {
    position: relative;
    width: 1200px;
    height: 3168px;
  }
  .cover {
    position: absolute;
    left: 175px;
    width: 835px;
    height: 835px;
    overflow: hidden;
    background: var(--red-deep);
    box-shadow: 34px 34px 8px var(--shadow);
  }
  .cover--star { top: 195px; }
  .cover--dots { top: 1161px; }
  .cover--fist { top: 2124px; }

  .cover__band {
    position: absolute;
    left: 0; top: 0;
    width: 100%;
    height: 278px;
    background: var(--gold);
  }
  .cover__backdrop {
    position: absolute;
    left: 0; right: 0; bottom: 0;
    top: 278px;
    background: radial-gradient(circle at 62% 0%,
      var(--red-bright) 0%,
      var(--red-mid) 40%,
      var(--red-deep) 80%,
      #1c0101 100%);
  }
  .cover__portrait {
    position: absolute;
    left: 0; top: 55px;
    width: 540px;
    height: 780px;
    background:
      radial-gradient(ellipse 120px 70px at 210px 70px, var(--hat-red) 0 98%, transparent 100%),
      linear-gradient(180deg, var(--grey-light) 0%, #5f5b57 35%, var(--grey-dark) 70%, #151413 100%);
    clip-path: polygon(30% 0%, 62% 0%, 68% 40%, 92% 52%, 100% 100%, 0% 100%, 0% 52%, 22% 40%);
  }

  .cover__title {
    position: absolute;
    left: 360px;
    right: 14px;
    top: 14px;
    margin: 0;
    font-family: "Outfit", sans-serif;
    font-weight: 800;
    color: var(--ink);
    text-align: right;
    white-space: nowrap;
  }
  .cover__title-small {
    display: block;
    font-size: 76px;
    line-height: 1;
    letter-spacing: -1px;
  }
  .cover__title-big {
    display: block;
    margin-top: 14px;
    font-size: 150px;
    line-height: 1;
    letter-spacing: -2px;
  }
  .cover__accent { color: var(--red-bright); }
  .cover__accent--badge {
    display: inline-block;
    padding: 0 0.14em 0 0.16em;
    margin: 0 0.02em;
    color: var(--cream);
    line-height: 1;
  }
  .cover--dots .cover__accent--badge {
    background: radial-gradient(circle at 50% 54%, var(--ink) 0, #3d3428 0.22em, #8a7636 0.38em, transparent 0.45em);
  }
  .cover--fist .cover__accent--badge {
    background: radial-gradient(circle at 50% 54%, var(--ink) 0 0.44em, transparent 0.45em);
  }

  .cover__host {
    position: absolute;
    right: 0;
    bottom: 6px;
    width: 326px;
    height: 75px;
    background: var(--gold);
    font-family: "Outfit", sans-serif;
    font-weight: 400;
    font-size: 50px;
    line-height: 75px;
    text-align: center;
    color: var(--ink);
  }
</style>
</head>
<body>
<main class="canvas">

  <section class="cover cover--star">
    <div class="cover__band"></div>
    <div class="cover__backdrop"></div>
    <div class="cover__portrait" role="img" aria-label="Black and white portrait of the host in a red cap, arms crossed"></div>
    <h1 class="cover__title">
      <span class="cover__title-small">Keep the</span>
      <span class="cover__title-big">H<span class="cover__accent">E</span>LM</span>
    </h1>
    <div class="cover__host">Dane Corwell</div>
  </section>

  <section class="cover cover--dots">
    <div class="cover__band"></div>
    <div class="cover__backdrop"></div>
    <div class="cover__portrait" role="img" aria-label="Black and white portrait of the host in a red cap, arms crossed"></div>
    <h1 class="cover__title">
      <span class="cover__title-small">Keep the</span>
      <span class="cover__title-big">H<span class="cover__accent cover__accent--badge" title="Halftone circle behind the letter">E</span>LM</span>
    </h1>
    <div class="cover__host">Dane Corwell</div>
  </section>

  <section class="cover cover--fist">
    <div class="cover__band"></div>
    <div class="cover__backdrop"></div>
    <div class="cover__portrait" role="img" aria-label="Black and white portrait of the host in a red cap, arms crossed"></div>
    <h1 class="cover__title">
      <span class="cover__title-small">Keep the</span>
      <span class="cover__title-big">H<span class="cover__accent cover__accent--badge" title="Raised fist emblem in a circle">E</span>LM</span>
    </h1>
    <div class="cover__host">Dane Corwell</div>
  </section>

</main>
</body>
</html>
```